Name of Business: KORL Advisory. It is a consulting and advisory business providing Investment and f

I am looking for a letterhead (preferably in word) design for a new business that portarys the attributes of professionalism, honesty, integrity and impartiality. I operate in a Regional area called Ocean Grove which is located about 90min drive from Melbourne CBD on the Victorian coast.

I have an open mind on design and colour: like all things creative it will either hit the spot or not.
Updates

Hi - Thank you all for your disigns. We are currently travelling in Australia and can't always get an internet coonnections. We are reviewing all designs and will try and get back to each of your over the next few days. Derek Plimsey

Industry/Entity Type

Business

```html
<!DOCTYPE html>
<html lang="en">
<head>
<meta charset="utf-8">
<title>KORL Advisory Letterhead</title>
<link rel="stylesheet" href="https://fonts.googleapis.com/css2?family=Mulish:wght@300;400&display=swap">
<style>
  :root {
    --ink: #000000;
    --paper: #ffffff;
    --rule: #6b1414;
    --accent-soft: #d9b9b9;
    --accent-fade: #f3e6e6;
    --footer-text: #1a1a1a;
  }
  * { margin: 0; padding: 0; box-sizing: border-box; }
  html, body {
    width: 867px;
    height: 1200px;
    overflow: hidden;
    background: var(--paper);
  }
  .letterhead {
    position: relative;
    width: 867px;
    height: 1200px;
    background: var(--paper);
    font-family: "Mulish", "Avenir", sans-serif;
  }
  .masthead {
    position: absolute;
    left: 0;
    top: 3px;
    width: 865px;
    height: 102px;
    background: var(--ink);
    border-top: 2px solid var(--rule);
    border-bottom: 3px solid var(--rule);
  }
  .brand-square {
    position: absolute;
    left: 50px;
    top: 44px;
    width: 32px;
    height: 32px;
    background: var(--paper);
  }
  .brand-name {
    position: absolute;
    left: 97px;
    top: 26px;
    color: var(--paper);
    font-weight: 300;
    font-size: 57px;
    line-height: 1;
    letter-spacing: 3px;
    white-space: nowrap;
  }
  .corner-accent {
    position: absolute;
    left: 638px;
    top: 945px;
    width: 212px;
    height: 209px;
    background: linear-gradient(135deg, var(--accent-fade) 0%, var(--accent-soft) 70%);
  }
  .footer-rule {
    position: absolute;
    left: 0;
    top: 1154px;
    width: 867px;
    height: 2px;
    background: var(--rule);
  }
  .contact {
    position: absolute;
    top: 1166px;
    font-size: 13.5px;
    font-weight: 400;
    line-height: 17px;
    letter-spacing: 1.2px;
    color: var(--footer-text);
  }
  .contact-address { left: 47px; }
  .contact-online { left: 364px; }
  .contact-phone { left: 702px; }
</style>
</head>
<body>
  <div class="letterhead">
    <header class="masthead">
      <div class="brand-square"></div>
      <div class="brand-name">KORL Advisory</div>
    </header>

    <div class="corner-accent" role="img" aria-label="Faint decorative brand motif in soft rose tones"></div>

    <div class="footer-rule"></div>

    <footer>
      <div class="contact contact-address">Address 1<br>Address 2</div>
      <div class="contact contact-online">website address<br>email address</div>
      <div class="contact contact-phone">Telephone<br>Mobile</div>
    </footer>
  </div>
</body>
</html>
```